Business card for IT company

Looking for a business card for an IT company providing server, network, and application support to medium businesses. Company name is Halvern Systems. Website is www.halvernsystems.example, would like to use the green color that is on the homepage. Prefer design to be done in Illustrator. Please, only DESIGNERS apply - no PHP programmers attempting to do design. Thank you

Industry/Entity Type

Information Technology

Requirements
Must have
• Green
Should not have
• Template designs, or designs done by non-designer type people

```html
<!DOCTYPE html>
<html lang="en">
<head>
<meta charset="utf-8">
<title>Halvern Systems – Business Card</title>
<link rel="stylesheet" href="https://fonts.googleapis.com/css2?family=Roboto:wght@300;400;700&display=swap">
<style>
  :root {
    --page-bg: #e4e4e4;
    --card-green: #7cbc25;
    --card-green-deep: #72b122;
    --ink-white: #ffffff;
    --ink-soft: rgba(255, 255, 255, 0.9);
    --ring-shade: rgba(40, 80, 10, 0.09);
    --card-shadow: rgba(0, 0, 0, 0.28);
  }
  * { box-sizing: border-box; margin: 0; padding: 0; }
  html, body {
    width: 1200px;
    height: 576px;
    overflow: hidden;
    background: var(--page-bg);
    font-family: "Roboto", Arial, sans-serif;
  }
  .canvas {
    position: relative;
    width: 1200px;
    height: 576px;
  }
  .card {
    position: absolute;
    top: 138px;
    width: 484px;
    height: 294px;
    overflow: hidden;
    background: linear-gradient(180deg, var(--card-green) 0%, var(--card-green-deep) 100%);
    box-shadow: 1px 3px 5px var(--card-shadow);
    color: var(--ink-white);
  }
  .card--front { left: 82px; }
  .card--back { left: 602px; }

  .decor-ring {
    position: absolute;
    width: 408px;
    height: 408px;
    border-radius: 50%;
    border: 16px solid var(--ring-shade);
    background: var(--ring-shade);
    top: -26px;
  }
  .card--front .decor-ring { left: 289px; }
  .card--back .decor-ring { left: -232px; }

  /* Brand lockups */
  .brand-mark {
    position: absolute;
    border-radius: 50%;
    background: var(--ink-white);
  }
  .brand-name {
    position: absolute;
    font-weight: 300;
    color: var(--ink-white);
    text-transform: uppercase;
    letter-spacing: 1px;
    line-height: 1;
  }
  .card--front .brand-mark { width: 96px; height: 96px; left: 194px; top: 74px; }
  .card--front .brand-name {
    left: 0; right: 0; top: 182px;
    text-align: center;
    font-size: 26px;
  }
  .card--back .brand-mark { width: 88px; height: 88px; left: 336px; top: 27px; }
  .card--back .brand-name {
    right: 24px; top: 152px;
    text-align: right;
    font-size: 21px;
  }

  /* Person */
  .person { position: absolute; left: 22px; top: 24px; }
  .person__name { font-size: 19px; font-weight: 700; line-height: 1.2; }
  .person__role { font-size: 11.5px; font-weight: 400; color: var(--ink-soft); margin-top: 3px; }

  /* Contact list */
  .contact {
    position: absolute;
    left: 22px;
    top: 218px;
    list-style: none;
  }
  .contact__item {
    display: flex;
    align-items: center;
    height: 17px;
    font-size: 12px;
    font-weight: 400;
    color: var(--ink-soft);
  }
  .contact__icon {
    width: 10px;
    height: 10px;
    margin-right: 12px;
    fill: var(--ink-soft);
    flex: none;
  }
</style>
</head>
<body>
<main class="canvas">

  <section class="card card--front" aria-label="Card front">
    <div class="decor-ring" aria-hidden="true"></div>
    <div class="brand-mark" aria-hidden="true"></div>
    <p class="brand-name">Halvern Systems</p>
  </section>

  <section class="card card--back" aria-label="Card back">
    <div class="decor-ring" aria-hidden="true"></div>
    <div class="person">
      <h1 class="person__name">Daniel Reyes</h1>
      <p class="person__role">Managing Director</p>
    </div>
    <div class="brand-mark" aria-hidden="true"></div>
    <p class="brand-name">Halvern Systems</p>
    <ul class="contact">
      <li class="contact__item">
        <svg class="contact__icon" viewBox="0 0 10 10" aria-hidden="true">
          <path d="M1 3.2 C1 1.6 2.4 1 5 1 C7.6 1 9 1.6 9 3.2 L7.2 3.6 L6.8 2.6 L3.2 2.6 L2.8 3.6 Z M2.6 4.4 L7.4 4.4 L8.6 8.8 L1.4 8.8 Z"/>
        </svg>
        555.014.2270
      </li>
      <li class="contact__item">
        <svg class="contact__icon" viewBox="0 0 10 10" aria-hidden="true">
          <path d="M5 0.5 A4.5 4.5 0 1 0 5 9.5 A4.5 4.5 0 1 0 5 0.5 Z M5 1.5 C5.8 2.3 6.2 3.5 6.3 4.5 L3.7 4.5 C3.8 3.5 4.2 2.3 5 1.5 Z M3.7 5.5 L6.3 5.5 C6.2 6.5 5.8 7.7 5 8.5 C4.2 7.7 3.8 6.5 3.7 5.5 Z M1.55 4.5 C1.7 3.2 2.5 2.1 3.6 1.7 C3 2.5 2.8 3.5 2.7 4.5 Z M1.55 5.5 L2.7 5.5 C2.8 6.5 3 7.5 3.6 8.3 C2.5 7.9 1.7 6.8 1.55 5.5 Z M7.3 4.5 C7.2 3.5 7 2.5 6.4 1.7 C7.5 2.1 8.3 3.2 8.45 4.5 Z M7.3 5.5 L8.45 5.5 C8.3 6.8 7.5 7.9 6.4 8.3 C7 7.5 7.2 6.5 7.3 5.5 Z"/>
        </svg>
        www.halvernsystems.example
      </li>
      <li class="contact__item">
        <svg class="contact__icon" viewBox="0 0 10 10" aria-hidden="true">
          <path d="M0.5 2 L9.5 2 L5 5.6 Z M0.5 2.9 L5 6.5 L9.5 2.9 L9.5 8 L0.5 8 Z"/>
        </svg>
        support@halvernsystems.example
      </li>
    </ul>
  </section>

</main>
</body>
</html>
```